WORD Template for Training Manual called Quiet Harvest

I have written a training manual called Quiet Harvest. I need a design for the manual I can put the materials into for small groups of people to use.
This means a cover along with a page design that looks appealing but doesn't distract from the content.
We already have an organisational logo and colour scheme. It would be great to have at nine different page designs as the manual will have nine sessions of learning. So one design for each session of content.
I have uploaded some of the example materials we have designed from another designer as well so you can see the kind of look and feel our other materials have.
I have also uploaded the introduction and the first session of the content so you can use it to help shape the design.
As you will see in the sessions, each session has small group activities, discussion questions and a video content session for the group to watch. All nine sessions will be designed in a similar way.
There will also be a second booklet to design of daily reflections so a successful design for this workbook will lead to a second project with the same look and feel.
Updates
Need extra days to review
Target Market(s)
My target market is adults from 18-45
Industry/Entity Type
Christian Ministry
Look and feel

```html
<!DOCTYPE html>
<html lang="en">
<head>
<meta charset="utf-8">
<title>Quiet Harvest – Session Template</title>
<link href="https://fonts.googleapis.com/css2?family=Poppins:wght@400;500;600;700&display=swap" rel="stylesheet">
<style>
:root{
  --green:#3dba6f;
  --green-light:#a3d15c;
  --green-dark:#34b574;
  --ink:#1d1d1d;
  --body:#3a3a3a;
  --muted:#555;
  --brand:#554a60;
  --paper:#ffffff;
}
*{box-sizing:border-box;margin:0;padding:0}
html,body{width:1200px;height:2574px;overflow:hidden;background:var(--paper)}
body{position:relative;font-family:"Poppins",sans-serif;color:var(--body)}
.block{position:absolute;left:75px;width:1055px}

/* masthead */
.brand{position:absolute;left:75px;top:52px;width:380px;display:flex;align-items:center;gap:16px}
.brand-dot{flex:none;width:62px;height:62px;border-radius:50%;background:var(--green)}
.brand-name{font-weight:600;font-size:30px;line-height:1.1;color:var(--brand);white-space:nowrap}
.masthead-title{position:absolute;left:497px;top:38px;width:620px}
.masthead-title h1{font-size:25px;font-weight:700;color:var(--green);line-height:36px}
.masthead-title p{font-size:19px;line-height:30px;color:var(--muted);letter-spacing:.3px}

/* green section band */
.band{position:absolute;left:75px;width:1052px;height:70px}
.band svg{position:absolute;inset:0}
.band h2{position:relative;padding:8px 0 0 20px;font-size:30px;font-weight:700;color:#fff;letter-spacing:.5px}

/* text */
.prose p{font-size:13.4px;line-height:26.5px;margin-bottom:9px;text-align:justify;letter-spacing:.25px}
.session-title{font-size:24px;font-weight:700;color:var(--green)}
.topic{font-size:20px;line-height:30px;color:var(--muted);letter-spacing:.3px}
.label{font-size:16px;font-weight:600;color:var(--ink)}
.sub-green{font-size:19px;font-weight:700;color:var(--green)}
.small{font-size:13.4px;line-height:24px;letter-spacing:.25px}

.num{display:flex;align-items:flex-start;font-size:13.4px;line-height:24px;letter-spacing:.25px}
.num-badge{flex:none;width:26px;height:26px;border-radius:50%;background:linear-gradient(var(--green-light),var(--green-dark));color:#fff;font-size:13px;font-weight:600;display:flex;align-items:center;justify-content:center;margin-right:31px;letter-spacing:0}
.tick{display:flex;align-items:flex-start;font-size:13.4px;line-height:24px;letter-spacing:.25px}
.tick svg{flex:none;margin:6px 15px 0 2px}
</style>
</head>
<body>

<header>
  <div class="brand">
    <span class="brand-dot"></span>
    <span class="brand-name">Fernway Ministries</span>
  </div>
  <div class="masthead-title">
    <h1>Quiet Harvest</h1>
    <p>60 Days of learning that will teach you to leap from safety into the adventure of your life!.</p>
  </div>
</header>

<svg width="0" height="0" style="position:absolute">
  <defs>
    <linearGradient id="bandFill" x1="0" y1="0" x2="0" y2="1">
      <stop offset="0" stop-color="#a3d15c"/>
      <stop offset="1" stop-color="#34b574"/>
    </linearGradient>
  </defs>
</svg>

<section>
  <div class="band" style="top:175px">
    <svg viewBox="0 0 1052 70" width="1052" height="70"><path d="M0 0H1052V68C900 58 700 56 520 62C330 69 150 70 0 60Z" fill="url(#bandFill)"/></svg>
    <h2>Introduction</h2>
  </div>
  <div class="block prose" style="top:262px">
    <p>When I was a young boy, I loved games and adventures. Games I played with Mum and Dad, and the adventures I read in books or created in my imagination and played out in the backyard. One of my favourite games was pretty simple. I would start at the end of the hallway in our house, Mum would call me, and I would run down the hallway as fast as I could. When I got to the end of the hallway, I would leap into the air through the doorway into the kitchen, and she would catch me and give me a great big hug.</p>
    <p>One day I put my fertile imagination and this game together and decided to play the game with Dad. Dad came home from work one afternoon through the front door and headed down the hallway to the kitchen. He stood in the kitchen in clear view and was chatting with Mum. I imagined what it would be like to play this game with Dad; in my head, it all played out beautifully.</p>
    <p>So, I yelled out, “Dad, Dad, ”and took off down the hallway as fast as my legs could carry me. Dad had a look in my direction and then looked back to Mum. I kept running down the hallway, and Dad looked back at me and waited for me to arrive; I got to the Kitchen doorway and leapt as high and as far as I had ever jumped in my life…</p>
    <p>I regained consciousness with blood running down my face and my dad saying, “I didn’t know the game”. Mum was trying to stop the bleeding, and my brain was struggling to figure out what had happened. It seems I had flown across the kitchen headfirst into the cupboards, cutting my head open on the cupboard door handle, a scar I retain to this day.</p>
    <p>For me, following Jesus can be a little like this, I think I have it figured out, and I embark on what I think God wants me to do; I hit my head and then wonder what on earth happened. At that point, wounded and bruised, God always brings me back to the basics. He calls me back to his simple commands to love others the way he loves me, to announce that He is here, that He loves others too, and to gather with other followers for worship, encouragement and support so we can follow Jesus together.</p>
    <p>Quiet Harvest takes followers of Jesus through those basic commands and their implications for our everyday life. My goal in developing this material is to teach you how to look at the world around you through Jesus’ eyes, to see people the way He sees them, and then to pursue His mission as a part of your everyday being and doing. To move beyond believing in God and accepting his Grace and Forgiveness to living his commands faithfully and, by doing so, being part of God’s transformation project, just like He always intended.</p>
  </div>
</section>

<section>
  <div class="band" style="top:927px">
    <svg viewBox="0 0 1052 70" width="1052" height="70"><path d="M0 0H1052V68C900 58 700 56 520 62C330 69 150 70 0 60Z" fill="url(#bandFill)"/></svg>
    <h2>Week One</h2>
  </div>

  <h3 class="block session-title" style="top:1012px">What is Love?</h3>
  <p class="block topic" style="top:1052px">Topic: Love is a choice, followed by an action to step into the world of another and act self-sacrificially in that person’s best interests.</p>

  <h4 class="block label" style="top:1136px">In this session, participants will learn to:</h4>
  <div class="block num" style="top:1176px"><span class="num-badge">1</span><span>Explain the biblical concept of Love as expressed by God through Jesus Christ</span></div>
  <div class="block num" style="top:1212px"><span class="num-badge">2</span><span>Describe how they can express love towards others in their context.</span></div>

  <h4 class="block label" style="top:1271px">Resources you will need:</h4>
  <p class="block small" style="top:1303px">A3 Paper for drawing and Coloured Pencils/Textas for drawing.</p>

  <h4 class="block label" style="top:1360px">Pre-video activity</h4>
  <p class="block small" style="top:1391px;text-align:justify">In groups of 3, draw a picture representing the moment the father welcomes his prodigal son home (Luke 15:11-32). Think about what it was the father was saying through his actions. What was the son saying through his actions? What was being expressed between them? This is not a picture of the moment like a photograph, but rather a picture representing it in a way that might not even have the father and son in it.</p>

  <h4 class="block label" style="top:1481px">Show Video Content for What is Love?</h4>

  <h4 class="block sub-green" style="top:1520px">Large Group Discussion</h4>
  <div class="block tick" style="top:1554px"><svg width="13" height="10" viewBox="0 0 13 10"><path d="M1 5l4 4 7-8" fill="none" stroke="#3dba6f" stroke-width="2"/></svg><span>Was there any content in the video that was new to you or expressed in a way that you hadn’t heard before?</span></div>
  <div class="block tick" style="top:1585px"><svg width="13" height="10" viewBox="0 0 13 10"><path d="M1 5l4 4 7-8" fill="none" stroke="#3dba6f" stroke-width="2"/></svg><span>What were the key points being made in the video?</span></div>

  <h4 class="block sub-green" style="top:1629px">Small Group Discussion</h4>
  <div class="block tick" style="top:1662px"><svg width="13" height="10" viewBox="0 0 13 10"><path d="M1 5l4 4 7-8" fill="none" stroke="#3dba6f" stroke-width="2"/></svg><span>Was there any content in the video that was new to you or expressed in a way that you hadn’t heard before?</span></div>
  <div class="block tick" style="top:1693px"><svg width="13" height="10" viewBox="0 0 13 10"><path d="M1 5l4 4 7-8" fill="none" stroke="#3dba6f" stroke-width="2"/></svg><span>What were the key points being made in the video?</span></div>

  <h4 class="block label" style="top:1757px">In groups of three, discuss the following questions.</h4>

  <div class="block num" style="top:1798px;width:1070px"><span class="num-badge">1</span><span>When Jesus was born, God entered our world. God incarnate, God in human flesh. This is the moment God's revolution began when God chose to come and dwell amongst us. This is the heart of God's mission, to go and live with His created humans.</span></div>
  <div class="block tick" style="top:1861px"><svg width="13" height="10" viewBox="0 0 13 10"><path d="M1 5l4 4 7-8" fill="none" stroke="#3dba6f" stroke-width="2"/></svg><span>What does it mean to you that God wants to live in your world and understand what life is like for you?</span></div>

  <div class="block num" style="top:1906px;width:1070px"><span class="num-badge">2</span><span>In doing this, God has expressed His love for each and every person He has created. Paul expressed this best in Romans 5:6-8, writing, "You see, just at the right time, when we were still powerless, Christ died for the ungodly. Very rarely will anyone die for a righteous person, though for a good person, someone might possibly dare to die. But God demonstrates his own love for us in this: While we were still sinners, Christ died for us.”</span></div>
  <div class="block tick" style="top:1993px"><svg width="13" height="10" viewBox="0 0 13 10"><path d="M1 5l4 4 7-8" fill="none" stroke="#3dba6f" stroke-width="2"/></svg><span>What does it mean to you that God’s love for you is something you haven’t and can’t earn?</span></div>
  <div class="block tick" style="top:2032px"><svg width="13" height="10" viewBox="0 0 13 10"><path d="M1 5l4 4 7-8" fill="none" stroke="#3dba6f" stroke-width="2"/></svg><span>What example does that set for each of us in how we love others?</span></div>

  <div class="block num" style="top:2076px;width:1070px"><span class="num-badge">3</span><span>To love someone means choosing to enter into their world in the same way that God entered into our world. Once we have chosen to do this, we pick up our cross and prepare to sacrifice our self-interests to benefit the other person whom Jesus loves.</span></div>
  <div class="block tick" style="top:2138px"><svg width="13" height="10" viewBox="0 0 13 10"><path d="M1 5l4 4 7-8" fill="none" stroke="#3dba6f" stroke-width="2"/></svg><span>What might this look like in practical terms? Is there an example of this you could think of and share?</span></div>
  <div class="block tick" style="top:2178px"><svg width="13" height="10" viewBox="0 0 13 10"><path d="M1 5l4 4 7-8" fill="none" stroke="#3dba6f" stroke-width="2"/></svg><span>What are some of the potential costs of living this way?</span></div>
</section>

<section>
  <div class="band" style="top:2244px">
    <svg viewBox="0 0 1052 70" width="1052" height="70"><path d="M0 0H1052V68C900 58 700 56 520 62C330 69 150 70 0 60Z" fill="url(#bandFill)"/></svg>
    <h2>Read Romans 5:1-5</h2>
  </div>
  <div class="block tick" style="top:2339px"><svg width="13" height="10" viewBox="0 0 13 10"><path d="M1 5l4 4 7-8" fill="none" stroke="#3dba6f" stroke-width="2"/></svg><span>Does anyone have an example to share of their decision to love someone causing personal suffering? Can you relate to what Paul has written about suffering leading to resilience, character, and hope?</span></div>

  <h4 class="block sub-green" style="top:2407px">Large Group Discussion</h4>
  <p class="block small" style="top:2441px">Share with the larger group what your group has learned together as you have worked through the questions.</p>
  <p class="block small" style="top:2472px">Close the evening with a time of prayer.</p>
</section>

</body>
</html>
```